International online gaming platform needs a game UI design

1. We need a game interface for three kinds of theme based on our guideline and sample mockup.
2. The product type is the online casino games related, we need a series of casino games UIs, however, we can start on the game lobby first.
3. Three theme you might choose from or refer to:
A. 3D look & feel
B. Realistic casino theme
C. Richness and grandeur
D. European casino style
4. NOT ALLOWED to change the design layout.
MUST follow our sample mock up and ONLY redefine the design style.
5. All items must be in a stand-alone component, eg. Button, Tab, Icon,... etc.
6. We need the layout in vector shape, but we can review in JPG or PNG format.
7. The image size: 1366 x 768

Updated:
1. All items and their positions should be same as the sample UI we provided.
Please redesign all the items and create a new theme for it.
No need to create a new layout.
2. Although we accept the draft design, but all the items in UI should be completed.
3. All the wordings in the sample UI are confirmed, you might change the fonts.
4. For the avatar in the left hand side, you don't have to redraw it.
We already have our own avatar system implemented.
5. All the items such as icons, tabs, and buttons are free to redesign.

Dear designers,

We've increased our budget and raise the prize money to 800 USD.  
We also accept the draft design in PNG format and we can go through the details in handover stage.
Thank you very much. 

Reason: Dear designers, We decided to extend the deadline by 7 days. As mentioned in the task description, we are looking for a new style of design and you might refer to the below style. A. 3D look & feel B. Realistic casino theme C. Richness and grandeur D. European casino style If you are still interested in our project, please send us your work. Thank you very much!

```html
<!DOCTYPE html>
<html lang="en">
<head>
<meta charset="utf-8">
<title>Live Casino Lobby</title>
<link href="https://fonts.googleapis.com/css2?family=Roboto+Condensed:wght@400;700&family=Roboto:wght@400;500;700&display=swap" rel="stylesheet">
<style>
:root{
  --bg-deep:#5a0014;
  --bg-mid:#a0062e;
  --bg-pink:#d81a63;
  --red:#c8102e;
  --red-dark:#7a0a14;
  --red-bright:#ee2233;
  --gold:#f0c040;
  --gold-light:#ffe58a;
  --gold-dark:#a8791a;
  --panel:#1b1b1b;
  --text:#ffffff;
  --text-dark:#1a1a1a;
}
*{box-sizing:border-box;margin:0;padding:0}
html,body{width:1200px;height:675px;overflow:hidden;background:var(--bg-deep)}
body{font-family:"Roboto",sans-serif;color:var(--text)}
.lobby{position:relative;width:1200px;height:675px;overflow:hidden;
  background:radial-gradient(ellipse at 55% 20%,var(--bg-pink) 0%,var(--bg-mid) 40%,var(--bg-deep) 100%)}
.abs{position:absolute}

/* header */
.brand{left:9px;top:8px;height:36px;display:flex;align-items:center;gap:8px;
  font-family:"Roboto Condensed",sans-serif;font-weight:700;font-size:34px;color:var(--text);letter-spacing:.5px}
.brand-dot{width:20px;height:20px;border-radius:50%;background:var(--text)}
.sys-icons{right:10px;top:7px;display:flex;gap:7px}
.sys-btn{width:27px;height:27px;border:2px solid var(--gold-dark);border-radius:3px;
  background:linear-gradient(var(--gold-light),var(--gold));display:flex;align-items:center;justify-content:center}
.sys-btn.close{background:linear-gradient(#ff5a3a,var(--red))}
.clock{left:7px;top:54px;width:267px;height:44px;border-radius:8px;border:2px solid #555;
  background:linear-gradient(#4a4a4a,#111);display:flex;align-items:center;justify-content:center;
  font-family:"Roboto Condensed",sans-serif;font-size:19px;color:var(--gold)}
.game-tab{top:46px;height:59px;border-radius:10px;border:2px solid var(--gold);
  background:linear-gradient(90deg,var(--red-dark),var(--red) 60%,#e83a4a);display:flex;align-items:center;
  font-family:"Roboto Condensed",sans-serif;font-weight:700;font-size:24px;color:var(--text)}
.game-tab.active{background:linear-gradient(90deg,#333,#555 60%,#2a2a2a)}
.tab-badge{width:62px;height:62px;margin-left:-4px;margin-right:16px;border-radius:50%;
  border:4px solid var(--gold);box-shadow:0 0 0 2px var(--gold-dark)}
.tab-art{position:absolute;right:6px;top:6px;width:52px;height:44px;border-radius:6px;opacity:.75}

/* left column */
.player-card{left:9px;top:123px;width:188px;height:264px;border-radius:8px;border:3px solid var(--red-dark);
  background:linear-gradient(var(--red),var(--red-dark))}
.avatar{left:24px;top:19px;width:134px;height:160px;border-radius:6px;border:3px solid var(--gold-dark);
  background:linear-gradient(#1c3a5a,#0c1a2a)}
.player-id{left:0;top:187px;width:100%;text-align:center;font-size:15px;color:var(--text)}
.profile-btn{left:16px;top:208px;width:156px;height:37px;border-radius:5px;border:1px solid #555;
  background:linear-gradient(#4a4a4a,#111);display:flex;align-items:center;justify-content:center;
  font-size:18px;color:var(--gold)}
.side-link{left:23px;width:158px;height:38px;border-radius:5px;border:1px solid #3a0008;
  background:linear-gradient(var(--red),var(--red-dark));display:flex;align-items:center;gap:6px;padding-left:7px;
  font-size:14px;letter-spacing:-.2px;white-space:nowrap;color:var(--gold-light)}
.side-icon{flex:none;width:18px;height:18px;border-radius:3px;background:var(--gold);display:flex;align-items:center;justify-content:center}
.side-art{left:25px;top:529px;width:182px;height:146px;border-radius:6px;
  background:linear-gradient(160deg,#d9c8a0,#8a6a3a 60%,#3a2a18)}

/* featured tables */
.feature{left:218px;top:125px;width:276px;height:133px;border-radius:8px;border:2px solid var(--gold);
  background:linear-gradient(var(--red-dark),var(--bg-deep))}
.strip{left:499px;top:127px;width:683px;height:126px;border-radius:8px;border:2px solid var(--gold);
  background:linear-gradient(var(--red),var(--red-dark))}
.dealer-card{top:14px;width:216px;height:98px;border-radius:6px;border:2px solid #666;background:#111}
.dealer-photo{border:2px solid var(--gold-dark);background:linear-gradient(#234a6e,#0d2236)}
.road{background:#fff}
.dealer-bar{display:flex;justify-content:space-between;align-items:center;background:#111;color:var(--text)}
.deals{background:var(--red-dark);height:100%;display:flex;align-items:center;padding:0 5px}

/* filter bar */
.filter-bar{left:218px;top:265px;width:964px;height:42px;border-radius:6px;border:2px solid var(--gold-dark);
  background:linear-gradient(#3a2a10,#1a1206)}
.multi-label{left:4px;top:4px;width:132px;height:31px;border-radius:4px;background:linear-gradient(var(--gold-light),var(--gold));
  color:var(--text-dark);font-size:15px;display:flex;align-items:center;gap:6px;padding-left:6px}
.filter-btn{top:7px;height:26px;border-radius:3px;border:1px solid var(--gold-dark);
  background:linear-gradient(var(--gold-light),var(--gold));color:var(--text-dark);font-size:14px;font-weight:500;
  display:flex;align-items:center;justify-content:center;gap:4px}

/* table cards */
.table-card{width:308px;height:166px;border-radius:6px;border:2px solid var(--red-bright);
  background:linear-gradient(var(--red) 0%,var(--red-dark) 26%,#2a0306 100%)}
.t-name{left:12px;top:4px;font-size:11px;font-weight:700}
.t-limit{left:12px;top:20px;font-size:11px;font-weight:700;color:var(--gold)}
.t-comm{right:10px;top:4px;font-size:11px;font-weight:700}
.t-range{right:10px;top:20px;font-size:11px;font-weight:700}
.join-btn{left:99px;top:16px;width:108px;height:42px;border-radius:6px;border:2px solid #888;
  background:linear-gradient(var(--red-bright),var(--red-dark));font-family:"Roboto Condensed",sans-serif;
  font-size:21px;font-weight:700;display:flex;align-items:center;justify-content:center;z-index:2}
.bet-table{left:6px;top:48px}
.seats{left:10px;top:131px;display:flex;gap:12px}
.pager{right:6px;top:128px;display:flex;gap:4px}
.pager span{width:42px;height:29px;border-radius:3px;background:linear-gradient(#ff4a3a,var(--red-dark));
  border:1px solid #ff7a6a;display:flex;align-items:center;justify-content:center}
</style>
</head>
<body>
<svg width="0" height="0" style="position:absolute" aria-hidden="true">
  <defs>
    <linearGradient id="felt" x1="0" y1="0" x2="0" y2="1"><stop offset="0" stop-color="#3a3a3a"/><stop offset="1" stop-color="#0a0a0a"/></linearGradient>
    <pattern id="grid" width="11" height="11" patternUnits="userSpaceOnUse"><path d="M11 0H0V11" fill="none" stroke="#ccc" stroke-width="1"/></pattern>
    <symbol id="table" viewBox="0 0 292 72">
      <polygon points="30,0 262,0 292,72 0,72" fill="url(#felt)" stroke="#555"/>
      <line x1="16" y1="34" x2="276" y2="34" stroke="#c8102e"/>
      <line x1="8" y1="53" x2="284" y2="53" stroke="#c8102e"/>
      <g stroke="#c8102e"><line x1="53" y1="34" x2="50" y2="72"/><line x1="91" y1="34" x2="89" y2="72"/><line x1="129" y1="34" x2="127" y2="72"/><line x1="166" y1="34" x2="166" y2="72"/><line x1="203" y1="34" x2="205" y2="72"/><line x1="241" y1="34" x2="243" y2="72"/></g>
      <g font-family="Roboto,sans-serif" font-style="italic" font-size="13" fill="#e52a3a" text-anchor="middle"><text x="34" y="48">B</text><text x="72" y="48">B</text><text x="110" y="48">B</text><text x="147" y="48">B</text><text x="184" y="48">B</text><text x="222" y="48">B</text><text x="260" y="48">B</text></g>
      <g font-family="Roboto,sans-serif" font-style="italic" font-size="13" fill="#f0c040" text-anchor="middle"><text x="30" y="67">P</text><text x="70" y="67">P</text><text x="108" y="67">P</text><text x="147" y="67">P</text><text x="186" y="67">P</text><text x="224" y="67">P</text><text x="264" y="67">P</text></g>
    </symbol>
    <symbol id="seat" viewBox="0 0 30 30">
      <circle cx="15" cy="9" r="7" fill="#f5c542"/>
      <path d="M3 28c0-8 5-11 12-11s12 3 12 11z" fill="#cfe6ff"/>
    </symbol>
    <symbol id="down" viewBox="0 0 24 20"><polygon points="2,2 22,2 12,18" fill="#a00812" stroke="#5a0008"/></symbol>
  </defs>
</svg>

<main class="lobby">
  <div class="abs brand"><span class="brand-dot"></span>LIVE CASINO</div>
  <div class="abs sys-icons">
    <span class="sys-btn"><svg width="17" height="17" viewBox="0 0 17 17"><rect x="1" y="1" width="15" height="15" rx="3" fill="none" stroke="#6a4a00" stroke-width="2"/><text x="8.5" y="13" font-size="11" font-weight="700" text-anchor="middle" fill="#6a4a00" font-family="Roboto,sans-serif">$</text></svg></span>
    <span class="sys-btn"><svg width="17" height="17" viewBox="0 0 17 17"><circle cx="7" cy="7" r="5" fill="none" stroke="#6a4a00" stroke-width="2"/><line x1="11" y1="11" x2="16" y2="16" stroke="#6a4a00" stroke-width="2.5"/></svg></span>
    <span class="sys-btn"><svg width="17" height="17" viewBox="0 0 17 17"><path d="M6 3l9-2v11" fill="none" stroke="#6a4a00" stroke-width="2"/><line x1="6" y1="3" x2="6" y2="14" stroke="#6a4a00" stroke-width="2"/><circle cx="4" cy="14" r="2.5" fill="#6a4a00"/><circle cx="13" cy="12" r="2.5" fill="#6a4a00"/></svg></span>
    <span class="sys-btn"><svg width="17" height="17" viewBox="0 0 17 17" fill="none" stroke="#6a4a00" stroke-width="2"><path d="M1 6V1h5M11 1h5v5M16 11v5h-5M6 16H1v-5"/></svg></span>
    <span class="sys-btn close"><svg width="15" height="15" viewBox="0 0 15 15" stroke="#fff" stroke-width="3"><line x1="2" y1="2" x2="13" y2="13"/><line x1="13" y1="2" x2="2" y2="13"/></svg></span>
  </div>
  <div class="abs clock">1/28/2014 06:54 PM GMT +8</div>

  <div class="abs game-tab active" style="left:288px;width:206px"><span class="tab-badge" style="background:radial-gradient(#fff,#bbb)" role="img" aria-label="Cards and chips icon"></span>Baccarat</div>
  <div class="abs game-tab" style="left:504px;width:208px"><span class="tab-badge" style="background:radial-gradient(#f3e6d0,#b09060)" role="img" aria-label="Dealer icon"></span>Super six</div>
  <div class="abs game-tab" style="left:720px;width:234px"><span class="tab-badge" style="background:radial-gradient(#c99a40,#5a3a10)" role="img" aria-label="Roulette wheel icon"></span>Roultee<span class="tab-art" style="background:linear-gradient(#6a0a14,#2a0206)" role="img" aria-label="Roulette table art"></span></div>
  <div class="abs game-tab" style="left:963px;width:228px"><span class="tab-badge" style="background:radial-gradient(#8aaacc,#2a4a6a)" role="img" aria-label="Dice cup icon"></span>Sic Bo<span class="tab-art" style="background:linear-gradient(#ff5a5a,#b00012)" role="img" aria-label="Red dice art"></span></div>

  <section class="abs player-card">
    <div class="abs avatar" role="img" aria-label="Player avatar"></div>
    <div class="abs player-id">ALPos 848767</div>
    <div class="abs profile-btn">Profile</div>
  </section>
  <div class="abs side-link" style="top:400px"><span class="side-icon"><svg width="12" height="12" viewBox="0 0 12 12"><path d="M1 4h3l4-3v10L4 8H1z" fill="#3a0008"/></svg></span>Announcements</div>
  <div class="abs side-link" style="top:446px"><span class="side-icon"><svg width="12" height="12" viewBox="0 0 12 12"><rect x="5" y="1" width="2" height="7" fill="#3a0008"/><rect x="5" y="9" width="2" height="2" fill="#3a0008"/></svg></span>Rules &amp; Regulation</div>
  <div class="abs side-link" style="top:489px"><span class="side-icon"><svg width="12" height="12" viewBox="0 0 12 12"><circle cx="5" cy="5" r="3.5" fill="none" stroke="#3a0008" stroke-width="1.6"/><line x1="8" y1="8" x2="11" y2="11" stroke="#3a0008" stroke-width="2"/></svg></span>Quick tour</div>
  <div class="abs side-art" role="img" aria-label="Illustrated king playing card"></div>

  <section class="abs feature">
    <div class="abs dealer-photo" style="left:8px;top:8px;width:84px;height:88px" role="img" aria-label="Dealer photo"></div>
    <svg class="abs road" style="left:96px;top:8px" width="170" height="88" viewBox="0 0 170 88">
      <rect width="170" height="88" fill="url(#grid)"/>
      <g fill="none" stroke-width="1.8">
        <circle cx="6" cy="5" r="4" stroke="#1a3fd6"/><circle cx="6" cy="16" r="4" stroke="#1a3fd6"/><circle cx="17" cy="5" r="4" stroke="#e52a3a"/><circle cx="17" cy="16" r="4" stroke="#e52a3a"/><circle cx="28" cy="5" r="4" stroke="#1a3fd6"/><circle cx="39" cy="5" r="4" stroke="#e52a3a"/><circle cx="50" cy="5" r="4" stroke="#1a3fd6"/><circle cx="61" cy="5" r="4" stroke="#e52a3a"/><circle cx="72" cy="5" r="4" stroke="#1a3fd6"/><circle cx="94" cy="5" r="4" stroke="#e52a3a"/><circle cx="105" cy="5" r="4" stroke="#1a3fd6"/><circle cx="116" cy="5" r="4" stroke="#1a3fd6"/><circle cx="116" cy="16" r="4" stroke="#1a3fd6"/><circle cx="127" cy="5" r="4" stroke="#e52a3a"/><circle cx="127" cy="16" r="4" stroke="#e52a3a"/><circle cx="127" cy="27" r="4" stroke="#e52a3a"/><circle cx="127" cy="38" r="4" stroke="#e52a3a"/><circle cx="127" cy="49" r="4" stroke="#e52a3a"/><circle cx="127" cy="60" r="4" stroke="#e52a3a"/><circle cx="138" cy="5" r="4" stroke="#1a3fd6"/><circle cx="138" cy="16" r="4" stroke="#1a3fd6"/>
      </g>
    </svg>
    <div class="abs dealer-bar" style="left:8px;top:102px;width:258px;height:22px;font-size:12px;padding-left:6px">Dealer Name<span class="deals">Deals 999</span></div>
  </section>

  <section class="abs strip">
    <div class="abs dealer-card" style="left:10px">
      <div class="abs dealer-photo" style="left:3px;top:3px;width:68px;height:68px" role="img" aria-label="Dealer photo"></div>
      <svg class="abs road" style="left:74px;top:3px" width="136" height="68" viewBox="0 0 136 68"><rect width="136" height="68" fill="url(#grid)"/><g fill="none" stroke-width="1.6"><circle cx="5" cy="5" r="3.5" stroke="#1a3fd6"/><circle cx="5" cy="16" r="3.5" stroke="#e52a3a"/><circle cx="16" cy="5" r="3.5" stroke="#e52a3a"/><circle cx="27" cy="5" r="3.5" stroke="#e52a3a"/><circle cx="38" cy="5" r="3.5" stroke="#1a3fd6"/><circle cx="49" cy="5" r="3.5" stroke="#1a3fd6"/></g></svg>
      <div class="abs dealer-bar" style="left:3px;top:75px;width:208px;height:18px;font-size:10px;padding-left:5px">Dealer Name<span class="deals">Deals 999</span></div>
    </div>
    <div class="abs dealer-card" style="left:234px">
      <div class="abs dealer-photo" style="left:3px;top:3px;width:68px;height:68px" role="img" aria-label="Dealer photo"></div>
      <svg class="abs road" style="left:74px;top:3px" width="136" height="68" viewBox="0 0 136 68"><rect width="136" height="68" fill="url(#grid)"/><g fill="none" stroke-width="1.6"><circle cx="5" cy="5" r="3.5" stroke="#1a3fd6"/><circle cx="5" cy="16" r="3.5" stroke="#1a3fd6"/><circle cx="5" cy="27" r="3.5" stroke="#1a3fd6"/><circle cx="16" cy="5" r="3.5" stroke="#e52a3a"/><circle cx="16" cy="16" r="3.5" stroke="#e52a3a"/><circle cx="27" cy="5" r="3.5" stroke="#1a3fd6"/><circle cx="38" cy="5" r="3.5" stroke="#e52a3a"/><circle cx="38" cy="16" r="3.5" stroke="#e52a3a"/><circle cx="49" cy="5" r="3.5" stroke="#1a3fd6"/><circle cx="60" cy="5" r="3.5" stroke="#1a3fd6"/></g></svg>
      <div class="abs dealer-bar" style="left:3px;top:75px;width:208px;height:18px;font-size:10px;padding-left:5px">Dealer Name<span class="deals">Deals 999</span></div>
    </div>
    <div class="abs dealer-card" style="left:458px">
      <div class="abs dealer-photo" style="left:3px;top:3px;width:68px;height:68px" role="img" aria-label="Dealer photo"></div>
      <svg class="abs road" style="left:74px;top:3px" width="136" height="68" viewBox="0 0 136 68"><rect width="136" height="68" fill="url(#grid)"/><g fill="none" stroke-width="1.6"><circle cx="5" cy="5" r="3.5" stroke="#1a3fd6"/><circle cx="16" cy="5" r="3.5" stroke="#e52a3a"/><circle cx="16" cy="16" r="3.5" stroke="#e52a3a"/><circle cx="27" cy="5" r="3.5" stroke="#1a3fd6"/><circle cx="38" cy="5" r="3.5" stroke="#e52a3a"/><circle cx="49" cy="5" r="3.5" stroke="#1a3fd6"/><circle cx="93" cy="5" r="3.5" stroke="#1a3fd6"/><circle cx="93" cy="16" r="3.5" stroke="#1a3fd6"/><circle cx="93" cy="27" r="3.5" stroke="#1a3fd6"/></g></svg>
      <div class="abs dealer-bar" style="left:3px;top:75px;width:208px;height:18px;font-size:10px;padding-left:5px">Dealer Name<span class="deals">Deals 999</span></div>
    </div>
  </section>

  <nav class="abs filter-bar">
    <div class="abs multi-label">Multiplayer<svg width="36" height="22" viewBox="0 0 36 22" fill="#1a1a1a"><circle cx="9" cy="7" r="4"/><circle cx="27" cy="7" r="4"/><circle cx="18" cy="6" r="5"/><path d="M2 21c0-6 3-8 7-8s7 2 7 8zM20 21c0-6 3-8 7-8s7 2 7 8z"/><path d="M9 22c0-7 4-10 9-10s9 3 9 10z"/></svg></div>
    <span class="abs filter-btn" style="left:450px;width:107px">Join any</span>
    <span class="abs filter-btn" style="left:560px;width:44px">A↔Z</span>
    <span class="abs filter-btn" style="left:608px;width:44px">$⬇</span>
    <span class="abs filter-btn" style="left:655px;width:42px">$⬆</span>
    <span class="abs filter-btn" style="left:704px;width:44px"><svg width="22" height="14" viewBox="0 0 22 14" fill="#1a1a1a"><circle cx="5" cy="4" r="3"/><circle cx="11" cy="4" r="3"/><circle cx="17" cy="4" r="3"/><path d="M0 14c0-5 2-6 5-6s5 1 5 6zM6 14c0-5 2-6 5-6s5 1 5 6zM12 14c0-5 2-6 5-6s5 1 5 6z"/></svg></span>
    <span class="abs filter-btn" style="left:752px;width:42px">&lt;3</span>
    <span class="abs filter-btn" style="left:798px;width:43px">&gt;3</span>
    <span class="abs filter-btn" style="left:845px;width:111px">All Limits <svg width="12" height="8" viewBox="0 0 12 8"><polygon points="0,0 12,0 6,8" fill="#1a1a1a"/></svg></span>
  </nav>

  <article class="abs table-card" style="left:220px;top:316px">
    <span class="abs t-name">Baccart A5-3C</span><span class="abs t-limit">Bet Limit</span>
    <span class="abs t-comm">Commission 0/7</span><span class="abs t-range">0/100</span>
    <span class="abs join-btn">JOIN</span>
    <svg class="abs bet-table" width="292" height="72"><use href="#table"/></svg>
    <div class="abs seats"><svg width="28" height="28"><use href="#seat"/></svg><svg width="28" height="28"><use href="#seat"/></svg><svg width="28" height="28"><use href="#seat"/></svg><svg width="28" height="28"><use href="#seat"/></svg><svg width="28" height="28"><use href="#seat"/></svg></div>
    <div class="abs pager"><span><svg width="22" height="18"><use href="#down"/></svg></span><span><svg width="22" height="18"><use href="#down"/></svg></span></div>
  </article>
  <article class="abs table-card" style="left:546px;top:316px">
    <span class="abs t-name">Baccart A5-3C</span><span class="abs t-limit">Bet Limit</span>
    <span class="abs t-comm">Commission 0/7</span><span class="abs t-range">0/100</span>
    <span class="abs join-btn">JOIN</span>
    <svg class="abs bet-table" width="292" height="72"><use href="#table"/></svg>
    <div class="abs seats"><svg width="28" height="28"><use href="#seat"/></svg><svg width="28" height="28"><use href="#seat"/></svg><svg width="28" height="28"><use href="#seat"/></svg><svg width="28" height="28"><use href="#seat"/></svg><svg width="28" height="28"><use href="#seat"/></svg></div>
    <div class="abs pager"><span><svg width="22" height="18"><use href="#down"/></svg></span><span><svg width="22" height="18"><use href="#down"/></svg></span></div>
  </article>
  <article class="abs table-card" style="left:873px;top:316px">
    <span class="abs t-name">Baccart A5-3C</span><span class="abs t-limit">Bet Limit</span>
    <span class="abs t-comm">Commission 0/7</span><span class="abs t-range">0/100</span>
    <span class="abs join-btn">JOIN</span>
    <svg class="abs bet-table" width="292" height="72"><use href="#table"/></svg>
    <div class="abs seats"><svg width="28" height="28"><use href="#seat"/></svg><svg width="28" height="28"><use href="#seat"/></svg><svg width="28" height="28"><use href="#seat"/></svg><svg width="28" height="28"><use href="#seat"/></svg><svg width="28" height="28"><use href="#seat"/></svg></div>
    <div class="abs pager"><span><svg width="22" height="18"><use href="#down"/></svg></span><span><svg width="22" height="18"><use href="#down"/></svg></span></div>
  </article>
  <article class="abs table-card" style="left:218px;top:495px">
    <span class="abs t-name">Baccart A5-3C</span><span class="abs t-limit">Bet Limit</span>
    <span class="abs t-comm">Commission 0/7</span><span class="abs t-range">0/100</span>
    <span class="abs join-btn">JOIN</span>
    <svg class="abs bet-table" width="292" height="72"><use href="#table"/></svg>
    <div class="abs seats"><svg width="28" height="28"><use href="#seat"/></svg><svg width="28" height="28"><use href="#seat"/></svg><svg width="28" height="28"><use href="#seat"/></svg><svg width="28" height="28"><use href="#seat"/></svg><svg width="28" height="28"><use href="#seat"/></svg></div>
    <div class="abs pager"><span><svg width="22" height="18"><use href="#down"/></svg></span><span><svg width="22" height="18"><use href="#down"/></svg></span></div>
  </article>
  <article class="abs table-card" style="left:545px;top:498px">
    <span class="abs t-name">Baccart A5-3C</span><span class="abs t-limit">Bet Limit</span>
    <span class="abs t-comm">Commission 0/7</span><span class="abs t-range">0/100</span>
    <span class="abs join-btn">JOIN</span>
    <svg class="abs bet-table" width="292" height="72"><use href="#table"/></svg>
    <div class="abs seats"><svg width="28" height="28"><use href="#seat"/></svg><svg width="28" height="28"><use href="#seat"/></svg><svg width="28" height="28"><use href="#seat"/></svg><svg width="28" height="28"><use href="#seat"/></svg><svg width="28" height="28"><use href="#seat"/></svg></div>
    <div class="abs pager"><span><svg width="22" height="18"><use href="#down"/></svg></span><span><svg width="22" height="18"><use href="#down"/></svg></span></div>
  </article>
  <article class="abs table-card" style="left:872px;top:497px">
    <span class="abs t-name">Baccart A5-3C</span><span class="abs t-limit">Bet Limit</span>
    <span class="abs t-comm">Commission 0/7</span><span class="abs t-range">0/100</span>
    <span class="abs join-btn">JOIN</span>
    <svg class="abs bet-table" width="292" height="72"><use href="#table"/></svg>
    <div class="abs seats"><svg width="28" height="28"><use href="#seat"/></svg><svg width="28" height="28"><use href="#seat"/></svg><svg width="28" height="28"><use href="#seat"/></svg><svg width="28" height="28"><use href="#seat"/></svg><svg width="28" height="28"><use href="#seat"/></svg></div>
    <div class="abs pager"><span><svg width="22" height="18"><use href="#down"/></svg></span><span><svg width="22" height="18"><use href="#down"/></svg></span></div>
  </article>
</main>
</body>
</html>
```